Coldforge Prime manufacturing Project

We are looking at getting a brand new design for a new company that deals in selling stainless tubing and other stainless still products such as handrails, Spigots, Balustrade Fittings
Glass, Glass fittings and Aluminium Channels

We require a very clean website that deals with the following colours:

Blue to light blues
Blacks
Greys to light Greys
Whites

We are open for other ideas BUT we *DO NOT* want any pinks, greens or bright colours except for backgrounds colours we have chosen above. (It can be solid, gradient or a subtle pattern)

YOU MUST KEEP THE LOGO AS IS. PLEASE DO NOT ALTER THE LOGO IN *ANY WAY* and the logo MUST be the same colours and fonts.

Logo is attached.

The site must contain these aspects:
jQuery Slider (Image slide show)
Top drop down Menus
Be no more than 900px wide
Text is to be to the w3C standards. (no special fonts)

We will chop up the design into html format. You just need to provide the PSD file.

The clients opposition is:
www.quorvatrim.example

Industry/Entity Type

It Company

Requirements
Nice to have
• Alter the logo in anyway

Files

```html
<!DOCTYPE html>
<html lang="en">
<head>
<meta charset="utf-8">
<title>Coldforge Prime Manufacturing Co. Ltd</title>
<link rel="stylesheet" href="https://fonts.googleapis.com/css2?family=Arimo:wght@400;700&display=swap">
<style>
:root{
  --blue-deep:#2b4c7c;
  --blue-mid:#4a6ea3;
  --blue-light:#7c9fd3;
  --blue-pale:#a9c2e6;
  --ink:#111;
  --grey-text:#444;
  --grey-line:#9a9a9a;
  --grey-soft:#e6e6e6;
  --grey-bar:#3c3c3c;
  --white:#fff;
}
*{box-sizing:border-box;margin:0;padding:0}
html,body{width:880px;height:1200px;overflow:hidden;background:var(--white)}
body{font-family:Arimo,Arial,sans-serif;color:var(--ink)}
.site{position:relative;width:880px;height:1200px;overflow:hidden}
ul{list-style:none}
a{color:inherit;text-decoration:none}

/* top bar */
.topbar{position:absolute;left:0;top:0;width:880px;height:33px;
  background:linear-gradient(#fafafa,#e2e2e2);display:flex;align-items:center;
  font-size:11px;color:#333;padding-left:10px}
.topbar .item{display:flex;align-items:center;gap:6px;margin-right:24px}
.topbar svg{fill:#444}
.social{position:absolute;right:10px;top:7px;display:flex;gap:3px}
.social span{width:19px;height:19px;border-radius:50%;background:var(--blue-mid);display:block}

/* header */
.masthead{position:absolute;left:0;top:33px;width:880px;height:156px;
  background:radial-gradient(ellipse at 55% 20%,#fff 0%,#f3f3f3 50%,#dcdcdc 100%)}
.brand{position:absolute;left:10px;top:14px;width:220px;text-align:center}
.brand .mark{width:84px;height:84px;border-radius:50%;background:var(--blue-deep);margin:0 auto 6px}
.brand .name{font-size:26px;font-weight:400;color:var(--ink);letter-spacing:.2px;white-space:nowrap}
.brand .sub{font-size:11px;color:var(--ink);letter-spacing:2px;margin-top:1px}
.hero-tubes{position:absolute;left:290px;top:10px;width:312px;height:146px;
  background:linear-gradient(90deg,#d7d7d7,#9c9c9c 20%,#eee 35%,#a5a5a5 55%,#f2f2f2 70%,#989898 90%,#dedede);
  opacity:.55}
.search{position:absolute;left:678px;top:121px;width:200px;height:23px;border:1px solid #bbb;
  background:var(--white);font-size:10px;color:#222;padding:6px 9px}
.search svg{position:absolute;right:6px;top:4px}

/* nav */
.mainnav{position:absolute;left:0;top:189px;width:879px;height:24px;
  background:linear-gradient(#7895c4,#3e5f95)}
.mainnav ul{display:flex;height:100%}
.mainnav li{height:100%;display:flex;align-items:center;justify-content:center;
  color:var(--white);font-size:11px;font-weight:700;border-right:1px solid #8da8d3}
.mainnav li.current{background:linear-gradient(#3e5f95,#2b4c7c);font-size:12px}

/* slider */
.slider{position:absolute;left:0;top:213px;width:880px;height:323px;background:var(--white)}
.slide-photo{position:absolute;left:196px;top:0;width:684px;height:323px;
  background:linear-gradient(90deg,#f6f6f6 0%,#bdbdbd 20%,#e9e9e9 35%,#8d8d8d 52%,#f0f0f0 62%,#9a9a9a 78%,#e4e4e4 92%,#f8f8f8)}
.slide-caption{position:absolute;left:12px;top:24px;color:#555;font-size:21px;line-height:22px}
.slide-caption h1{font-size:29px;font-weight:400;color:#555;line-height:30px;letter-spacing:-.5px}
.slide-arrows{position:absolute;right:24px;top:279px;display:flex;gap:2px}
.slide-arrows span{width:25px;height:25px;background:var(--blue-mid);display:flex;align-items:center;justify-content:center}
.slider-shadow{position:absolute;left:30px;top:536px;width:820px;height:30px;
  background:radial-gradient(ellipse at 50% 0%,rgba(0,0,0,.22),rgba(0,0,0,0) 70%)}

/* content */
.content h2{position:absolute;top:585px;font-size:17px;font-weight:700;color:var(--blue-deep);letter-spacing:.3px}
.col{position:absolute;top:615px;font-size:11px;line-height:14.7px;color:var(--ink);white-space:nowrap}
.col p{margin-bottom:14.7px}
.divider{position:absolute;top:587px;width:1px;height:340px;background:var(--grey-line)}
.btn{display:inline-block;background:linear-gradient(#6f8fc2,#34568a);color:var(--white);
  font-size:11px;font-weight:700;padding:7px 8px;border:1px solid #2b4c7c}
.events .date{position:absolute;left:598px;font-size:11px;color:#333}
.events .thumb{position:absolute;left:598px;width:107px;border:1px solid #bbb;padding:3px}
.events .thumb div{width:100%;height:100%;background:linear-gradient(135deg,#e8e8e8,#8b8b8b 45%,#dcdcdc 70%,#707070)}
.events .blurb{position:absolute;left:711px;width:165px;font-size:11px;line-height:13.6px;white-space:nowrap}
.events .more{position:absolute;left:711px;background:linear-gradient(#6f8fc2,#34568a);color:var(--white);
  font-size:9px;width:78px;height:16px;display:flex;align-items:center;justify-content:center}
.events .rule{position:absolute;left:598px;top:773px;width:272px;border-top:1px dashed #bbb}

/* footer */
.footer{position:absolute;left:0;top:963px;width:880px;height:209px;
  background:linear-gradient(#88abdd,#5b7fb6 45%,#3a5a8c);color:var(--white)}
.footer h3{position:absolute;top:24px;font-size:18px;font-weight:400}
.footer .vline{position:absolute;top:27px;height:160px;border-left:1px dotted #c9d8ef}
.footer-menu{position:absolute;left:42px;top:59px;font-size:10px;line-height:19.7px}
.tweet{position:absolute;left:176px;width:220px;height:56px}
.tweet .avatar{position:absolute;left:3px;top:0;width:52px;height:52px;border-radius:50%;background:var(--blue-deep);border:3px solid #d8d8d8}
.tweet p{position:absolute;left:72px;top:6px;font-size:11.5px;line-height:14px;width:160px;white-space:nowrap}
.tweet time{position:absolute;left:165px;top:54px;font-size:8.5px}
.contact-list{position:absolute;left:428px;top:57px;font-size:12px}
.contact-list li{display:flex;gap:8px;align-items:flex-start;margin-bottom:10px;line-height:12.5px}
.contact-list svg{fill:var(--white);flex:none}
.newsletter input{position:absolute;left:642px;top:61px;width:196px;height:32px;border:1px solid #aaa;
  padding:0 8px;font-family:inherit;font-size:12px;color:#222;background:#f7f7f7}
.newsletter button{position:absolute;left:642px;top:107px;width:73px;height:26px;border:none;
  background:linear-gradient(#7996c7,#3a5b90);color:var(--white);font-family:inherit;font-size:12px}
.copyright{position:absolute;left:0;top:1172px;width:880px;height:28px;background:var(--grey-bar);
  color:var(--white);font-size:11px;display:flex;align-items:center;justify-content:center}
</style>
</head>
<body>
<div class="site">

  <div class="topbar">
    <span class="item"><svg width="12" height="15" viewBox="0 0 12 15"><circle cx="6" cy="5.5" r="4.5" fill="none" stroke="#444" stroke-width="2"/><rect x="5" y="10" width="2" height="5"/></svg>your address here your address here</span>
    <span class="item"><svg width="16" height="14" viewBox="0 0 16 14"><path d="M3 1l3 1-1 3c1 2 3 4 5 5l3-1 1 3-2 2C6 13 1 8 1 3z"/></svg>123 456 7890 123</span>
    <span class="item"><svg width="15" height="12" viewBox="0 0 15 12"><path d="M0 4l7.5-4 7.5 4v8H0z"/><path d="M1 5l6.5 4 6.5-4" fill="none" stroke="#fff"/></svg>info@youremail.com</span>
    <div class="social"><span></span><span></span><span></span><span></span></div>
  </div>

  <header class="masthead">
    <div class="brand">
      <div class="mark"></div>
      <div class="name">Coldforge Prime</div>
      <div class="sub">Manufacturing Co. Ltd</div>
    </div>
    <div class="hero-tubes" role="img" aria-label="Row of polished stainless steel tubes with angled cut ends"></div>
    <div class="search">SEARCH
      <svg width="15" height="15" viewBox="0 0 15 15"><circle cx="6" cy="6" r="4.5" fill="none" stroke="#333" stroke-width="1.5"/><path d="M9.5 9.5L14 14" stroke="#333" stroke-width="1.8"/></svg>
    </div>
  </header>

  <nav class="mainnav">
    <ul>
      <li class="current" style="width:76px">HOME</li>
      <li style="width:76px">ABOUT</li>
      <li style="width:97px">SERVICES</li>
      <li style="width:98px">PRODUST</li>
      <li style="width:102px">PARTNERS</li>
      <li style="width:111px">CONTACT US</li>
    </ul>
  </nav>

  <section class="slider">
    <div class="slide-photo" role="img" aria-label="Stainless steel beverage urns and polished glass spigots on flanged bases"></div>
    <div class="slide-caption">
      <h1>SPIGOTS</h1>
      Some text here Some text here<br>Some text here
    </div>
    <div class="slide-arrows">
      <span><svg width="10" height="12" viewBox="0 0 10 12"><path d="M7 1L2 6l5 5" fill="none" stroke="#fff" stroke-width="2.2"/></svg></span>
      <span><svg width="10" height="12" viewBox="0 0 10 12"><path d="M3 1l5 5-5 5" fill="none" stroke="#fff" stroke-width="2.2"/></svg></span>
    </div>
  </section>
  <div class="slider-shadow"></div>

  <main class="content">
    <h2 style="left:9px">WHO WE ARE?</h2>
    <div class="col" style="left:9px;width:240px">
      <p>Some text here Some text here Some text here<br>Some text here Some text here Some text here.</p>
      <p>Some text here Some text here Some text here<br>Some text here Some text here Some text here<br>Some text here Some text here Some text here<br>Some text here Some text here Some text here<br>Some text here Some text here Some text here<br>Some text here Some text here Some text here<br>Some text here Some text here Some text here<br>Some text here Some text here Some text here<br>Some text here Some text here Some text here<br>Some text here Some text here Some text here<br>Some text here Some text here Some text here</p>
      <p>Some text here Some text here Some text here<br>Some text here Some text here Some text here<br>Some text here.</p>
      <a class="btn" href="#">Read More...</a>
    </div>
    <div class="divider" style="left:268px"></div>

    <h2 style="left:303px">WHAT WE DO?</h2>
    <div class="col" style="left:303px;width:240px">
      <p>Some text here Some text here Some text here<br>Some text here Some text here Some text here.</p>
      <p>Some text here Some text here Some text here<br>Some text here Some text here Some text here<br>Some text here Some text here Some text here<br>Some text here Some text here Some text here<br>Some text here Some text here Some text here<br>Some text here Some text here Some text here<br>Some text here Some text here Some text here<br>Some text here Some text here Some text here<br>Some text here Some text here Some text here<br>Some text here Some text here Some text here<br>Some text here Some text here Some text here</p>
      <p>Some text here Some text here Some text here<br>Some text here Some text here Some text here<br>Some text here.</p>
      <a class="btn" href="#">Read More...</a>
    </div>
    <div class="divider" style="left:562px"></div>

    <h2 style="left:598px">UPCOMING EVENTS</h2>
    <section class="events">
      <div class="date" style="top:614px">June 1, 2013</div>
      <div class="thumb" style="top:631px;height:130px"><div role="img" aria-label="Bundle of stainless steel tubes seen end on"></div></div>
      <p class="blurb" style="top:628px">Some text here Some text here<br>Some text here Some text here<br>Some text here Some text here<br>Some text here Some text here<br>Some text here Some text here<br>Some text here Some text here<br>Some text here Some text here<br>Some text here Some text here<br>Some text here Some text here</p>
      <a class="more" href="#" style="top:753px">Read More...</a>
      <div class="rule"></div>
      <div class="date" style="top:783px">July 1, 2013</div>
      <div class="thumb" style="top:799px;height:129px"><div role="img" aria-label="Set of stainless steel cooking pots with lids"></div></div>
      <p class="blurb" style="top:798px">Some text here Some text here<br>Some text here Some text here<br>Some text here Some text here<br>Some text here Some text here<br>Some text here Some text here<br>Some text here Some text here<br>Some text here Some text here<br>Some text here Some text here<br>Some text here Some text here</p>
      <a class="more" href="#" style="top:923px">Read More...</a>
    </section>
  </main>

  <footer class="footer">
    <h3 style="left:42px">Menu</h3>
    <ul class="footer-menu">
      <li>HOME</li><li>ABOUT US</li><li>PICK-UP SERVICES</li><li>HOW IT WORKS</li><li>REQUEST A PICK-UP</li><li>CONTACT US</li>
    </ul>
    <div class="vline" style="left:157px"></div>

    <h3 style="left:176px">Recet Tweets</h3>
    <div class="tweet" style="top:54px">
      <div class="avatar"></div>
      <p>“Some text herre<br>Some text herre Some text”<br>(http://lnk.example/xR4tQ2)</p>
      <time>10 min ago</time>
    </div>
    <div class="tweet" style="top:132px">
      <div class="avatar"></div>
      <p>“Some text herre<br>Some text herre Some text”<br>(http://lnk.example/xR4tQ2)</p>
    </div>
    <div class="vline" style="left:409px"></div>

    <h3 style="left:428px">Contact us</h3>
    <ul class="contact-list">
      <li><svg width="16" height="14" viewBox="0 0 16 14"><path d="M3 1l3 1-1 3c1 2 3 4 5 5l3-1 1 3-2 2C6 13 1 8 1 3z"/></svg>123 45 678900</li>
      <li><svg width="15" height="12" viewBox="0 0 15 12"><path d="M0 4l7.5-4 7.5 4v8H0z"/><path d="M1 5l6.5 4 6.5-4" fill="none" stroke="#5b7fb6"/></svg>info@youremail.com</li>
      <li><svg width="14" height="22" viewBox="0 0 14 22"><circle cx="7" cy="8" r="5.5" fill="none" stroke="#fff" stroke-width="2"/><rect x="6" y="14" width="2" height="8"/></svg>Your adress here Your adress<br>here Your adress here</li>
    </ul>
    <div class="vline" style="left:625px"></div>

    <h3 style="left:642px">Sign up for our Newsletter</h3>
    <form class="newsletter">
      <input type="text" value="Email address" aria-label="Email address">
      <button type="button">Subscribe</button>
    </form>
  </footer>

  <div class="copyright">Copyright 2013 COLDFORGE PRIME &nbsp;I&nbsp; All Rights Reserved &nbsp;I&nbsp; Leader in Stainless Steel Products</div>
</div>
</body>
</html>
```